need professional, precise design for a website

I will start with a homepage design and if we pick your design, we'll have you design up to 6 more interior pages (we'll pay extra for these of course). We need a homepage design for a reserve study company based in Idaho, covering the northwest region. The company is called copper ridge reserve study. Their current site is at https://www.copperridgereserves.example/ and they really like this site for inspiration https://www.fundplannerhub.example/ but they would like an original design, just more modern and fresh like the sample site. I have logo files I will attach. They want something that looks financial and has a feel of accuity. Their main call to action will be to have someone fill in a contact form or call them on the phone. They will have a sample study that someone can download as on the fundplannerhub site. You can use copy from their current site.

```html
<!DOCTYPE html>
<html lang="en">
<head>
<meta charset="utf-8">
<title>Copper Ridge Reserves — Reserve Studies</title>
<link href="https://fonts.googleapis.com/css2?family=Montserrat:wght@400;500;600&display=swap" rel="stylesheet">
<style>
  :root{
    --navy:#1e1a56;
    --ink:#3b3b4a;
    --muted:#6a6a74;
    --nav:#7a7a84;
    --white:#ffffff;
    --rule:#c9c8dc;
    --frame:#e6e6ea;
    --hero-a:#5d7884;
    --hero-b:#33454b;
    --slide-a:#5f8fbf;
    --slide-b:#7fa9b8;
    --tone-hoa-a:#b89a86;
    --tone-hoa-b:#9a7a66;
    --tone-com-a:#6f93b8;
    --tone-com-b:#8a6a66;
    --tone-park-a:#5f8a3f;
    --tone-park-b:#78a848;
  }
  *{box-sizing:border-box;margin:0;padding:0}
  html,body{width:693px;height:1200px;overflow:hidden}
  body{position:relative;font-family:'Montserrat',sans-serif;background:var(--white);color:var(--ink)}
  .abs{position:absolute}

  /* header */
  .site-header{position:absolute;left:0;top:0;width:693px;height:35px;background:var(--white);box-shadow:0 1px 3px rgba(0,0,0,.15);z-index:2}
  .brand{left:132px;top:12px;display:flex;align-items:center;gap:4px;font-size:9px;font-weight:500;color:var(--navy);letter-spacing:.2px}
  .brand-dot{width:9px;height:9px;border:1px solid var(--navy);border-radius:50%}
  .nav-link{position:absolute;top:14px;font-size:5.6px;color:var(--nav);letter-spacing:.3px}
  .nav-link.active::after{content:"";position:absolute;left:-1px;right:-1px;top:20px;height:1px;background:var(--ink)}

  /* hero */
  .hero{left:0;top:35px;width:693px;height:355px;border-bottom:2px solid var(--navy);
    background:linear-gradient(90deg,var(--hero-a) 0%,var(--hero-b) 100%)}
  .hero-title{left:0;width:693px;top:34px;text-align:center;color:var(--white);font-size:13.6px;font-weight:500;line-height:15.5px;letter-spacing:.8px}
  .hero-slide{left:130px;top:83px;width:433px;height:244px;border:1px solid #d8d8d8;
    background:linear-gradient(180deg,var(--slide-a) 0%,var(--slide-b) 100%)}
  .slide-dots{left:484px;top:332px;display:flex;gap:2px}
  .slide-dots span{width:8px;height:4px;border:1px solid #e9e9ee}
  .slide-dots span.on{background:var(--white)}

  /* studies */
  .study-photo{width:180px;height:104px;border:2px solid var(--frame)}
  .photo-hoa{background:linear-gradient(180deg,var(--tone-hoa-a),var(--tone-hoa-b))}
  .photo-commercial{background:linear-gradient(180deg,var(--tone-com-a),var(--tone-com-b))}
  .photo-parks{background:linear-gradient(180deg,var(--tone-park-a),var(--tone-park-b))}
  .study-title{font-size:9.6px;font-weight:600;color:var(--navy);letter-spacing:.8px;white-space:nowrap}
  .study-text{font-size:5.3px;line-height:7px;color:var(--muted)}
  .right{text-align:right}
  .btn{height:12px;font-size:4.6px;display:flex;align-items:center;justify-content:center;border:1px solid var(--navy)}
  .btn-solid{background:var(--navy);color:var(--white)}
  .btn-outline{background:var(--white);color:var(--navy)}

  /* contact */
  .contact{left:0;top:801px;width:693px;height:399px;background:var(--navy);color:var(--white)}
  .contact-title{left:0;width:693px;top:26px;text-align:center;font-size:13.6px;font-weight:500}
  .field-label{left:238px;font-size:6px}
  .field-line{left:238px;width:216px;height:1px;background:var(--rule)}
  .send{left:238px;top:244px;width:216px;height:18px;background:var(--white);color:var(--navy);display:flex;align-items:center;justify-content:center;gap:6px;font-size:5.6px}
  .or{left:0;width:693px;top:286px;text-align:center;font-size:9.5px}
  .call{left:0;width:693px;top:317px;display:flex;justify-content:center;align-items:center;gap:6px;font-size:10.5px;font-weight:500}
  .copyright{left:0;width:693px;top:377px;text-align:center;font-size:4.2px;color:#c8c6e0;font-family:'Montserrat',sans-serif}
</style>
</head>
<body>

<header class="site-header">
  <div class="abs brand"><span class="brand-dot"></span>Copper Ridge Reserves</div>
  <nav>
    <span class="nav-link" style="left:372px">Home</span>
    <span class="nav-link active" style="left:408px">About</span>
    <span class="nav-link" style="left:445px">Reserve</span>
    <span class="nav-link" style="left:486px">Studies</span>
    <span class="nav-link" style="left:527px">Contact Us</span>
  </nav>
</header>

<section class="abs hero" role="img" aria-label="Blurred backdrop of the featured property photo">
  <h1 class="abs hero-title">YOUR FINANCIAL ROAD MAP<br>FOR THE NEXT 30 YEARS!</h1>
  <div class="abs hero-slide" role="img" aria-label="Photo: resort condominium with palm trees and a swimming pool"></div>
  <div class="abs slide-dots"><span></span><span></span><span></span><span></span><span></span><span></span><span></span><span class="on"></span></div>
</section>

<main>
  <div class="abs study-photo photo-hoa" style="left:130px;top:418px" role="img" aria-label="Photo: row of brick townhomes"></div>
  <h2 class="abs study-title" style="left:346px;top:437px">HOA &amp; Condominium Studies</h2>
  <p class="abs study-text" style="left:346px;top:454px;width:158px">Every homeowners association is different. Different sets of assets, different financials and different historical backgrounds that have brought you to the present. Each of these is taken into consideration to customize your 30 year budget and build the most accurate, most precise long-term savings ("reserve") report you can buy.</p>
  <div class="abs btn btn-solid" style="left:398px;top:509px;width:68px">Download Sample</div>
  <div class="abs btn btn-outline" style="left:469px;top:509px;width:35px">More</div>

  <div class="abs study-photo photo-commercial" style="left:382px;top:545px" role="img" aria-label="Photo: modern office tower"></div>
  <h2 class="abs study-title right" style="left:147px;width:200px;top:569px">Commercial, Vacation &amp; Time Share</h2>
  <p class="abs study-text right" style="left:158px;top:586px;width:189px">Your property represents a significant capital investment. In many cases, your business is dependent on the livelihood and functionality of the edifice in which it resides. We believe a fiscally sound plan and budget of capital expenses is as essential as the building itself. We are comprehensive, thorough and intense about our calculations.</p>
  <div class="abs btn btn-outline" style="left:157px;top:636px;width:35px">More</div>
  <div class="abs btn btn-solid" style="left:194px;top:636px;width:69px">Download Sample</div>

  <div class="abs study-photo photo-parks" style="left:130px;top:672px" role="img" aria-label="Photo: public park with lawn and playground"></div>
  <h2 class="abs study-title" style="left:346px;top:689px">Parks &amp; Public Lands</h2>
  <p class="abs study-text" style="left:346px;top:706px;width:156px">Your property represents a significant capital investment. In many cases, your business is dependent on the livelihood and functionality of the edifice in which it resides. We believe a fiscally sound plan and budget of capital expenses is as essential as the building itself. We are comprehensive, thorough and intense about our calculations.</p>
  <div class="abs btn btn-solid" style="left:398px;top:764px;width:68px">Download Sample</div>
  <div class="abs btn btn-outline" style="left:469px;top:764px;width:35px">More</div>
</main>

<section class="abs contact">
  <h2 class="abs contact-title">Contact Us</h2>
  <span class="abs field-label" style="top:67px">Name</span>
  <div class="abs field-line" style="top:90px"></div>
  <span class="abs field-label" style="top:105px">E-Mail</span>
  <div class="abs field-line" style="top:129px"></div>
  <span class="abs field-label" style="top:144px">Phone</span>
  <div class="abs field-line" style="top:166px"></div>
  <span class="abs field-label" style="top:181px">Message</span>
  <div class="abs field-line" style="top:232px"></div>
  <div class="abs send">
    <svg width="11" height="9" viewBox="0 0 11 9" aria-hidden="true"><path d="M0 0 L11 4.5 L0 9 L1.5 5.2 L6 4.5 L1.5 3.8 Z" fill="#1e1a56"/></svg>
    Send Message
  </div>
  <div class="abs or">Or</div>
  <div class="abs call">
    <svg width="15" height="15" viewBox="0 0 16 16" aria-hidden="true"><circle cx="8" cy="8" r="8" fill="#fff"/><path d="M5.2 3.8c.4-.3.9-.2 1.1.2l.8 1.4c.2.4.1.8-.2 1.1l-.5.4c.5 1.1 1.4 2 2.5 2.5l.4-.5c.3-.3.7-.4 1.1-.2l1.4.8c.4.2.5.7.2 1.1l-.6.8c-.4.5-1 .7-1.6.5-2.4-.8-4.3-2.7-5.1-5.1-.2-.6 0-1.2.5-1.6z" fill="#1e1a56"/></svg>
    Call Us (208) 555-0142
  </div>
  <p class="abs copyright">Copyright Copper Ridge Reserves, LLC © 2019 All Rights Reserved</p>
</section>

</body>
</html>
```